Online Prescription Eyeglass Lens Company Needs a Website

*Update new name to ClearPair. Thx

We are eye doctors with a lab that need a website for a new company based in Southern California called ClearPair. We replace old prescription lenses with new ones next day for most lenses. Patients select the lenses and give us the prescription. We then send a box with a prepaid shipping label. Place the frames in the box and drop them in the mail to our lab. We will custom make new lenses, fit them back into your frames and send them back to you. We would like to compete with www.vizora.com and offer affordable lenses for single vision, bifocal, progressive, sunglass lenses at an affordable price with next day shipping.
Updates

Hi Designers, We have a new name called ClearPair. Can we have the website design reflect the new name and we'll pick our favorites. Thx

Update: The new name is OptiNova . I have not made very many changes or feedback to the submissions because we were bidding for a .com. We won and our new name is OptiNova . This is the last name change.. Please have the website reflect the new name and I'll be providing feedback on the websites . ( I have a separate project for the logo people are working on, so don't worry about creating a logo). Look forward to the submissions. Thanks everyone.

Hi, Just leave the name as ClearPair for now. I will narrow down top designs tonight. Thx

Target Market(s)

Anyone that wears prescription or nonprescription glasses or sunglasses that want next day shipping.

Industry/Entity Type

Eyewear

Number of Pages Required

4 page

Font styles to use
Serif

Colors

Designer to choose colors to be used in the design.

Requirements
Must have
• I need a website that can compete with https://www.vizora.com/.
• We are different from vizora because we can offer same day service or next day shipping.
• It needs to have website that offers the lenses available listed below.
• Needs to be able to upload a prescription and payment feature.
• Pictures of different types of options with small info about each lens option.
• Template Pricing (just use numbers from $79-$179 for now)
• SINGLE VISION LENSES
• HIGH INDEX LENSES
• READING LENSES
• DIGITAL HD PROGRESSIVE LENSES
• RX & NON-RX SUNGLASSES
• RX & NON-RX POLARIZED SUNGLASSES
• COMPUTER LENSES
• TRANSITION LENSES
• BI-FOCAL LENSES

```html
<!DOCTYPE html>
<html lang="en">
<head>
<meta charset="utf-8">
<title>ClearPair – Our Process</title>
<link href="https://fonts.googleapis.com/css2?family=Cinzel:wght@400&family=Libre+Baskerville:wght@400;700&family=Open+Sans:wght@400;600&family=Josefin+Sans:wght@400;600&display=swap" rel="stylesheet">
<style>
:root{
  --navy:#4f6285;
  --navy-dark:#3f5580;
  --sky:#6cbdd9;
  --sky-deep:#4fa9cf;
  --icon:#a9c1e3;
  --ink:#4a4a4a;
  --muted:#8a8a8a;
  --band:#5f7399;
  --cta:#2a84c9;
  --footer:#1c1c1c;
  --white:#ffffff;
}
*{margin:0;padding:0;box-sizing:border-box}
html,body{width:781px;height:1200px;overflow:hidden;background:var(--white)}
.page{position:relative;width:781px;height:1200px;font-family:"Libre Baskerville",serif;color:var(--ink)}
.abs{position:absolute}

/* header */
.site-header{position:absolute;left:0;top:0;width:781px;height:61px;background:var(--white)}
.brand{position:absolute;left:71px;top:18px;font-family:"Cinzel",serif;font-size:26px;color:#2d3b55;letter-spacing:.5px;line-height:1}
.main-nav{position:absolute;left:316px;top:29px;display:flex;gap:12px;font-family:"Open Sans",sans-serif;font-size:8.5px;color:#6b6b6b;letter-spacing:.1px;white-space:nowrap}
.main-nav .current{color:var(--navy-dark)}
.order-btn{position:absolute;left:624px;top:23px;width:101px;height:25px;background:var(--navy);border-radius:4px;color:var(--white);font-size:8.5px;font-weight:700;display:flex;align-items:center;justify-content:center;letter-spacing:.3px}

/* hero */
.hero{position:absolute;left:0;top:61px;width:781px;height:268px;background:linear-gradient(90deg,var(--sky) 0%,#63b8d8 55%,var(--sky-deep) 100%)}
.hero-photo{position:absolute;left:390px;top:0;width:391px;height:268px;background:radial-gradient(ellipse at 55% 45%,#e9c2ae 0%,#c98d72 22%,#6a4a3c 38%,rgba(79,169,207,0) 62%)}
.hero-title{position:absolute;left:71px;top:53px;font-family:"Libre Baskerville",serif;font-weight:400;font-size:27px;color:var(--white);letter-spacing:.3px}
.hero-lead{position:absolute;left:72px;top:91px;width:240px;font-family:"Open Sans",sans-serif;font-size:9.5px;line-height:14px;color:#2c3e50;letter-spacing:-.2px}
.hero-price{position:absolute;left:72px;top:126px;font-size:14px;color:#3b4d66}
.hero-price b{font-weight:700}
.btn-light{position:absolute;top:153px;height:25px;background:var(--white);color:#333;font-size:7.5px;display:flex;align-items:center;justify-content:center}
.btn-view{position:absolute;left:73px;top:188px;width:229px;height:28px;background:var(--navy);color:var(--white);font-size:9px;display:flex;align-items:center;justify-content:center}

/* how it works */
.section-title{position:absolute;left:0;width:781px;top:363px;text-align:center;font-size:20px;font-weight:400;color:var(--navy-dark)}
.section-sub{position:absolute;left:0;width:781px;top:394px;text-align:center;font-size:10px;color:var(--muted)}
.section-sub b{color:#555}
.step-label{position:absolute;font-size:9.5px;color:#555;text-align:center;width:160px}

/* call to action band */
.cta-band{position:absolute;left:0;top:782px;width:781px;height:177px;background:linear-gradient(180deg,#6f84a8 0%,var(--band) 100%)}
.cta-title{position:absolute;left:0;width:781px;top:50px;text-align:center;font-size:22px;font-weight:400;color:var(--white);letter-spacing:-.5px}
.cta-btn{position:absolute;left:303px;top:88px;width:167px;height:34px;background:var(--cta);color:var(--white);font-size:11px;display:flex;align-items:center;justify-content:center;letter-spacing:-.2px}

/* footer */
.site-footer{position:absolute;left:0;top:959px;width:781px;height:241px;background:var(--footer);color:#d8d8d8}
.footer-brand{position:absolute;left:71px;top:61px;font-family:"Cinzel",serif;font-size:25px;color:var(--white);line-height:1}
.social{position:absolute;left:76px;top:99px;display:flex;gap:10px}
.social span{width:8px;height:8px;background:#e6e6e6;border-radius:1px}
.copyright{position:absolute;left:71px;top:138px;font-family:"Open Sans",sans-serif;font-size:8px;color:#e0e0e0;letter-spacing:-.3px}
.footer-col{position:absolute;top:61px;font-family:"Josefin Sans",sans-serif}
.footer-col h4{font-size:10px;font-weight:600;letter-spacing:1.3px;color:var(--white);margin-bottom:12px}
.footer-col li{list-style:none;font-size:8px;letter-spacing:.8px;line-height:13.5px;color:#cfcfcf}
.contact li{display:flex;align-items:center;gap:9px}
.contact svg{width:7px;height:7px;fill:#cfcfcf}
.footer-rule{position:absolute;left:71px;top:181px;width:651px;height:1px;background:#333}
</style>
</head>
<body>
<div class="page">

  <header class="site-header">
    <div class="brand">ClearPair</div>
    <nav class="main-nav">
      <span>OUR LENSES</span><span>WHY CLEARPAIR</span><span>THE LAB</span><span class="current">OUR PROCESS</span><span>&#9679; SIGN IN</span>
    </nav>
    <div class="order-btn">ORDER LENSES</div>
  </header>

  <section class="hero">
    <div class="hero-photo" role="img" aria-label="Smiling woman wearing clear-framed prescription glasses against a blue backdrop"></div>
    <h1 class="hero-title">OUR PROCESS</h1>
    <p class="hero-lead">Get the lenses you need, in your own frames, without leaving home.</p>
    <p class="hero-price">Starting at <b>$79-$179</b> for now</p>
    <div class="btn-light" style="left:72px;width:111px">CHOOSE YOUR LENSES</div>
    <div class="btn-light" style="left:192px;width:110px">SEE HOW IT'S DONE</div>
    <div class="btn-view">VIEW ALL LENS</div>
  </section>

  <h2 class="section-title">HOW CLEARPAIR WORKS</h2>
  <p class="section-sub">your new lenses delivered back at your door in <b>around 1 day.</b></p>

  <svg class="abs" style="left:0;top:0" width="781" height="782" viewBox="0 0 781 782">
    <g stroke="#555" stroke-width="1" stroke-dasharray="4 4" fill="none">
      <line x1="334" y1="470" x2="394" y2="470"/>
      <line x1="400" y1="508" x2="469" y2="508"/>
      <line x1="330" y1="596" x2="398" y2="596"/>
      <line x1="400" y1="660" x2="469" y2="660"/>
    </g>
    <line x1="398" y1="425" x2="398" y2="742" stroke="#ddd" stroke-width="1"/>
    <g fill="var(--navy)">
      <circle cx="324" cy="469" r="8.5"/><circle cx="477" cy="508" r="8.5"/>
      <circle cx="322" cy="596" r="8.5"/><circle cx="477" cy="660" r="8.5"/>
    </g>
    <g fill="#fff" font-family="Libre Baskerville,serif" font-size="9" text-anchor="middle">
      <text x="324" y="472">1</text><text x="477" y="511">2</text>
      <text x="322" y="599">3</text><text x="477" y="663">4</text>
    </g>
    <g fill="var(--icon)">
      <rect x="241" y="465" width="65" height="4" rx="2"/>
      <path d="M242 467 h26 v10 q0 12 -13 12 q-13 0 -13 -12z"/>
      <path d="M280 467 h26 v10 q0 12 -13 12 q-13 0 -13 -12z"/>
      <rect x="498" y="471" width="59" height="59"/>
      <rect x="502" y="484" width="51" height="42" fill="#fff"/>
      <rect x="507" y="489" width="41" height="32"/>
      <rect x="511" y="500" width="24" height="2" fill="#fff"/>
      <rect x="511" y="507" width="32" height="2" fill="#fff"/>
      <rect x="511" y="513" width="28" height="2" fill="#fff"/>
      <rect x="246" y="580" width="59" height="42"/>
      <rect x="253" y="594" width="20" height="2.5" fill="#fff"/>
      <rect x="253" y="600" width="16" height="2.5" fill="#fff"/>
      <rect x="289" y="591" width="9" height="8" fill="#fff"/>
      <path d="M520 640 l20 -10 l20 8 v30 l-20 10 l-20 -8z"/>
      <circle cx="516" cy="668" r="10" fill="#fff"/>
      <circle cx="516" cy="668" r="8"/>
      <path d="M511 668 l4 4 l7 -8" stroke="#fff" stroke-width="2" fill="none"/>
    </g>
  </svg>

  <p class="step-label" style="left:198px;top:501px">Pick Your Lenses</p>
  <p class="step-label" style="left:448px;top:539px">Fill out prescription</p>
  <p class="step-label" style="left:195px;top:634px">Mail Your Frames</p>
  <p class="step-label" style="left:460px;top:686px">Sight, Sealed, Delivered.</p>

  <section class="cta-band" role="img" aria-label="Blurred eye chart letters behind a call to action">
    <h2 class="cta-title">START SEEING CLEARLY</h2>
    <div class="cta-btn">SHOP THE LENSES</div>
  </section>

  <footer class="site-footer">
    <div class="footer-brand">ClearPair</div>
    <div class="social"><span></span><span></span><span></span><span></span></div>
    <p class="copyright">2017 all rights reserved</p>

    <div class="footer-col" style="left:270px">
      <h4>QUICK LINKS</h4>
      <ul><li>Eyeglasses</li><li>Sunglasses</li><li>Prescription sunglasses</li><li>Contact lenses</li></ul>
    </div>
    <div class="footer-col" style="left:449px">
      <h4>SHOP</h4>
      <ul><li>Shipping</li><li>Returns &amp; Exchanges</li><li>Price Matching</li><li>Privacy Policy</li><li>Warranty</li><li>Gift Service</li></ul>
    </div>
    <div class="footer-col contact" style="left:600px">
      <h4>CONTACT US</h4>
      <ul>
        <li><svg viewBox="0 0 10 10"><path d="M2 0 l2 2 l-1 2 q1 2 3 3 l2 -1 l2 2 l-2 2 q-7 -1 -8 -8z"/></svg>+1 (888) 555-0142</li>
        <li><svg viewBox="0 0 10 10"><rect x="0" y="3" width="10" height="7"/><rect x="2" y="0" width="6" height="3"/></svg>+1 (800) 555-0187</li>
        <li><svg viewBox="0 0 10 10"><path d="M0 1 h10 v8 h-10z M1 2 l4 3 l4 -3" fill="none" stroke="#cfcfcf" stroke-width="1"/></svg>hello@clearpairmail.com</li>
      </ul>
    </div>
    <div class="footer-rule"></div>
  </footer>

</div>
</body>
</html>
```